Bodywork Quietude Business Card Design

I want to create a very elegant and sophisticated two sided business card for my massage practice (www.bodyworkquietude.net). I have attached the logo and a PDF with some ideas down for the back of the card but I am open to suggestions. I will want to tie in a post card and flyer to the card later.
Similar colors to website would be great.
Target Market(s)
High end clientele, people looking for a sophisticated spa experience.
Industry/Entity Type
Massage
Contact Information for Business Card
Bodywork Quietude
7318 Larkspur Ave S, Suite 305
Seattle, WA 98103
(206) 555-0147
www.bodyworkquietude.net
Look and feel

```html
<!DOCTYPE html>
<html lang="en">
<head>
<meta charset="utf-8">
<title>Bodywork Quietude – Business Card</title>
<link href="https://fonts.googleapis.com/css2?family=Noto+Serif&family=Cinzel:wght@700&family=Ropa+Sans&family=Signika:wght@300&display=swap" rel="stylesheet">
<style>
  :root {
    --stage: #b9c8c9;
    --front-dark: #050606;
    --front-mid: #1f2223;
    --ink-light: #ffffff;
    --ink-navy: #10293d;
    --ink-dark: #1c1c1c;
    --band-blue: #2596e8;
    --band-blue-light: #3aa4ee;
    --accent-yellow: #f5b800;
    --paper: #ffffff;
  }
  * { box-sizing: border-box; margin: 0; padding: 0; }
  html, body { width: 1200px; height: 1200px; overflow: hidden; }
  body { background: var(--stage); position: relative; }

  .card {
    position: absolute;
    left: 158px;
    width: 868px;
    height: 508px;
    overflow: hidden;
    box-shadow: 0 2px 3px rgba(0,0,0,0.35);
  }
  .card--front {
    top: 46px;
    background: radial-gradient(ellipse at 62% 12%, var(--front-mid) 0%, var(--front-dark) 62%);
    color: var(--ink-light);
    text-align: center;
  }
  .card--back { top: 602px; background: var(--paper); }

  .brand-name {
    position: absolute;
    left: 0; right: 0;
    font-family: "Noto Serif", serif;
    font-size: 34px;
    letter-spacing: 0.5px;
    text-align: center;
  }
  .card--front .brand-name { top: 166px; color: var(--ink-light); }
  .card--back .brand-name { top: 102px; color: var(--ink-navy); }

  .front-invite {
    position: absolute;
    top: 332px; left: 40px; right: 40px;
    font-family: "Noto Serif", serif;
    font-size: 28px;
    line-height: 36px;
  }
  .front-service {
    position: absolute;
    top: 442px; left: 0; right: 0;
    font-family: "Cinzel", serif;
    font-weight: 700;
    font-size: 27px;
    letter-spacing: 0.5px;
  }

  .accent-rule {
    position: absolute;
    top: 252px; left: 0; width: 100%; height: 4px;
    background: var(--accent-yellow);
  }
  .accent-notch {
    position: absolute;
    top: 255px; left: 680px;
    width: 0; height: 0;
    border-left: 12px solid transparent;
    border-right: 12px solid transparent;
    border-top: 12px solid var(--accent-yellow);
    z-index: 2;
  }
  .contact-band {
    position: absolute;
    top: 256px; left: 0; width: 100%; height: 190px;
    background: radial-gradient(ellipse at 55% 45%, var(--band-blue-light) 0%, var(--band-blue) 60%);
  }
  .contact-list {
    position: absolute;
    top: 22px; left: 40px;
    list-style: none;
    font-family: "Ropa Sans", sans-serif;
    font-size: 24px;
    color: var(--ink-light);
  }
  .contact-list li {
    display: flex; align-items: center;
    height: 37.5px;
  }
  .contact-list svg { width: 20px; height: 20px; margin-right: 13px; flex: none; }
  .band-name {
    position: absolute;
    right: 40px; top: 74px;
    font-family: "Signika", sans-serif;
    font-weight: 300;
    font-size: 33px;
    color: var(--ink-light);
  }
  .address {
    position: absolute;
    top: 458px; left: 0; right: 0;
    text-align: center;
    font-family: "Noto Serif", serif;
    font-size: 27px;
    color: var(--ink-dark);
  }
</style>
</head>
<body>

<section class="card card--front">
  <div class="brand-name">Bodywork Quietude</div>
  <p class="front-invite">Come and Experience the Most Relaxing and Invitingly Deep Massage of Your Life.....</p>
  <p class="front-service">Deep Lomi Ultra Relaxation Massage</p>
</section>

<section class="card card--back">
  <div class="brand-name">Bodywork Quietude</div>
  <div class="accent-rule"></div>
  <div class="accent-notch"></div>
  <div class="contact-band" role="img" aria-label="Blue band with a soft honeycomb texture">
    <ul class="contact-list">
      <li>
        <svg viewBox="0 0 20 20" fill="#fff"><path d="M2 7c0-2 3-4 8-4s8 2 8 4v2h-4V7H6v2H2z"/><rect x="4" y="10" width="12" height="7" rx="2"/></svg>
        (206) 555-0147
      </li>
      <li>
        <svg viewBox="0 0 20 20" fill="#fff"><rect x="1" y="7" width="3" height="11"/><rect x="5" y="3" width="14" height="15"/><rect x="8" y="10" width="2" height="2" fill="#2596e8"/><rect x="12" y="10" width="2" height="2" fill="#2596e8"/><rect x="8" y="14" width="2" height="2" fill="#2596e8"/><rect x="12" y="14" width="2" height="2" fill="#2596e8"/></svg>
        000-111-2222
      </li>
      <li>
        <svg viewBox="0 0 20 20" fill="#fff"><path d="M2 8l8-6 8 6v10H2z"/><path d="M2 8l8 6 8-6" fill="none" stroke="#2596e8" stroke-width="1.5"/></svg>
        support@bodyworkquietude.net
      </li>
      <li>
        <svg viewBox="0 0 20 20" fill="none" stroke="#fff" stroke-width="1.6"><circle cx="10" cy="10" r="8"/><ellipse cx="10" cy="10" rx="3.5" ry="8"/><path d="M2 10h16M3.5 6h13M3.5 14h13"/></svg>
        www.bodyworkquietude.net
      </li>
    </ul>
    <div class="band-name">Bodywork Quietude</div>
  </div>
  <p class="address">7318 Larkspur Ave S, Suite 305 Seattle, WA 98103</p>
</section>

</body>
</html>
```